Kettle Ledger Business Card design

We need a stand out business card design for Accounting practice based in Australia specialising in pubs, clubs and hotels. We help venues maximise margins, create time and manage cashflow. One club we have been working with for the last 6 months has increased revenue by 3% and margin by 5% in this time frame. We have a back office outsourced system that costs less than having a full time employee and also allows the venues the added benefit of:<br/>-using the office space to become a revenue generating opportunity. <br/>-a complete system to enhance governance, accountability and efficiency within their operation<br/>-52 weeks cover so no hassle to cover annual/sick .. leave<br/><br/>We would like to see designs that use the colours of our logo (green & blue).
Target Market(s)
Australian Pubs, Clubs & Hotels abookkeeping, accounting and tax services
Industry/Entity Type
Accountant
Contact Information for Business Card
Miriam Oakley CPA
Principal
Accountant Tax Agent
Miriam@KettleLedger-example.com.au
0418693142
www.kettleledger-example.com.au
Accounting / Payroll / Tax / SMSF / Technology
Colors
Designer to choose colors to be used in the design.
Look and feel
Each slider illustrates characteristics of the customer's brand and the style your logo design should communicate.

```html
<!DOCTYPE html>
<html lang="en">
<head>
<meta charset="utf-8">
<title>Kettle Ledger Business Card</title>
<link href="https://fonts.googleapis.com/css2?family=Poppins:wght@700&family=Open+Sans:wght@400;600&display=swap" rel="stylesheet">
<style>
  :root {
    --backdrop: #3c3b3a;
    --brand-blue: #1e3a86;
    --brand-green: #17783a;
    --paper: #f4f4f4;
    --ink: #2a2a2a;
    --rule: #b9b9b9;
    --white: #ffffff;
  }
  * { margin: 0; padding: 0; box-sizing: border-box; }
  html, body { width: 1200px; height: 960px; overflow: hidden; }
  body {
    background: var(--backdrop);
    position: relative;
    font-family: "Open Sans", sans-serif;
  }
  .card {
    position: absolute;
    width: 560px;
    height: 342px;
    border-radius: 3px;
    overflow: hidden;
    box-shadow: 0 14px 30px rgba(0,0,0,.35);
  }
  /* Front side */
  .card--front {
    left: 50px; top: 130px;
    background: var(--brand-blue);
  }
  .front-mark {
    position: absolute;
    left: 0; right: 0; top: 120px;
    display: flex; align-items: center; justify-content: center; gap: 16px;
  }
  .mark-dot {
    width: 30px; height: 30px; border-radius: 50%;
    background: var(--brand-green);
  }
  .wordmark {
    font-family: "Poppins", sans-serif;
    font-weight: 700;
    font-size: 44px;
    letter-spacing: -0.5px;
    line-height: 1;
  }
  .card--front .wordmark { color: var(--white); }
  .front-web {
    position: absolute;
    left: 0; right: 0; bottom: 46px;
    text-align: center;
    color: var(--white);
    font-size: 13px;
    letter-spacing: 4px;
  }
  /* Back side */
  .card--back {
    left: 600px; top: 480px;
    background: radial-gradient(circle at 50% 35%, #ffffff 0%, var(--paper) 60%, #e6e6e6 100%);
  }
  .back-mark {
    position: absolute;
    left: 30px; top: 118px;
    display: flex; align-items: center; gap: 10px;
  }
  .back-mark .mark-dot { width: 20px; height: 20px; }
  .card--back .wordmark { color: var(--brand-blue); font-size: 28px; }
  .divider {
    position: absolute;
    left: 276px; top: 70px;
    width: 1px; height: 142px;
    background: var(--rule);
  }
  .contact {
    position: absolute;
    left: 296px; top: 76px;
  }
  .contact-name { color: var(--brand-blue); font-size: 17px; line-height: 1.2; }
  .contact-role { color: var(--brand-green); font-size: 15px; line-height: 1.2; margin-bottom: 12px; }
  .contact-line {
    display: flex; align-items: center; gap: 10px;
    color: var(--ink); font-size: 11.5px; line-height: 1; margin-bottom: 10px;
  }
  .contact-line svg { width: 15px; height: 15px; flex: none; }
  .band-rule {
    position: absolute; left: 0; right: 0; bottom: 54px;
    height: 2px; background: var(--brand-green);
  }
  .band {
    position: absolute; left: 0; right: 0; bottom: 0;
    height: 48px; background: var(--brand-blue);
  }
</style>
</head>
<body>
  <section class="card card--front">
    <div class="front-mark">
      <span class="mark-dot"></span>
      <span class="wordmark">Kettle Ledger</span>
    </div>
    <p class="front-web">www.kettleledger-example.com.au</p>
  </section>

  <section class="card card--back">
    <div class="back-mark">
      <span class="mark-dot"></span>
      <span class="wordmark">Kettle Ledger</span>
    </div>
    <div class="divider"></div>
    <div class="contact">
      <p class="contact-name">Miriam Oakley CPA</p>
      <p class="contact-role">Principal</p>
      <p class="contact-line">
        <svg viewBox="0 0 16 16" fill="none" stroke="#1e3a86" stroke-width="1.2"><path d="M3 2l3 1 1 3-2 1c1 2 2 3 4 4l1-2 3 1 1 3c-1 1-2 1-3 1C6 13 3 10 2 5c0-1 0-2 1-3z"/></svg>
        0418693142
      </p>
      <p class="contact-line">
        <svg viewBox="0 0 16 16" fill="none" stroke="#1e3a86" stroke-width="1.2"><rect x="1.5" y="3.5" width="13" height="9"/><path d="M1.5 3.5l6.5 5 6.5-5"/></svg>
        Miriam@KettleLedger-example.com.au
      </p>
      <p class="contact-line">
        <svg viewBox="0 0 16 16" fill="none" stroke="#1e3a86" stroke-width="1.2"><circle cx="8" cy="8" r="6.5"/><ellipse cx="8" cy="8" rx="3" ry="6.5"/><path d="M1.5 8h13M2.5 5h11M2.5 11h11"/></svg>
        www.kettleledger-example.com.au
      </p>
    </div>
    <div class="band-rule"></div>
    <div class="band"></div>
  </section>
</body>
</html>
```